I need a certificate for print - for completion of a course

I need someone to design for me a certificate printable on 8.5 x 11" card stock paper.

The design is for a permanent makeup course. I have attached my own certificate for an example. I am not 100% happy with my design, but the verbiage must stay the same.

I have also attached other certificates that I really like from other companies.

I want this certificate to be special. The colors for my company is pink and white. www.lashvellora.com

Target Market(s)

beauty industry

Industry/Entity Type

Makeup

Requirements
Must have
• Beautiful imagery. Pink and white

```html
<!DOCTYPE html>
<html lang="en">
<head>
<meta charset="utf-8">
<title>Certificate of Excellence</title>
<link href="https://fonts.googleapis.com/css2?family=Cinzel:wght@400&family=Cormorant+Garamond:wght@400;500&family=Parisienne&display=swap" rel="stylesheet">
<style>
  :root {
    --page: #ffffff;
    --white: #ffffff;
    --blush: #fbe3ec;
    --petal: #f4b8cc;
    --rose: #e07a9e;
    --pink: #cf4f80;
    --berry: #a8305f;
    --magenta: #c23a8c;
    --gold: #c59a62;
    --gold-light: #e9c995;
    --panel: #ffffff;
  }
  * { margin: 0; padding: 0; box-sizing: border-box; }
  html, body { width: 1200px; height: 800px; overflow: hidden; background: var(--page); }
  .canvas { position: relative; width: 1200px; height: 800px; }
  .certificate {
    position: absolute; left: 134px; top: 22px; width: 976px; height: 756px; overflow: hidden;
    background:
      radial-gradient(ellipse 300px 170px at 400px 90px, rgba(255,255,255,.55), transparent 70%),
      radial-gradient(ellipse 260px 240px at 40px 260px, rgba(255,255,255,.35), transparent 70%),
      radial-gradient(ellipse 300px 220px at 60px 700px, rgba(194,58,140,.75), transparent 70%),
      radial-gradient(ellipse 380px 160px at 400px 720px, rgba(168,48,95,.55), transparent 70%),
      linear-gradient(165deg, var(--rose) 0%, var(--pink) 45%, var(--berry) 100%);
  }
  .imagery {
    position: absolute; right: 0; top: 0; width: 430px; height: 100%;
    background:
      radial-gradient(ellipse 170px 240px at 270px 400px, rgba(255,240,244,.95), transparent 75%),
      radial-gradient(ellipse 260px 200px at 300px 80px, rgba(255,255,255,.6), transparent 70%),
      linear-gradient(200deg, var(--petal) 0%, var(--rose) 55%, var(--magenta) 100%);
    -webkit-mask-image: linear-gradient(90deg, transparent 0%, #000 32%);
            mask-image: linear-gradient(90deg, transparent 0%, #000 32%);
  }
  .frame { position: absolute; left: 0; top: 0; width: 976px; height: 756px; }
  .title {
    position: absolute; left: 0; top: 140px; width: 792px; text-align: center;
    font-family: "Cinzel", serif; font-weight: 400; font-size: 34px; letter-spacing: .5px;
    color: var(--white); line-height: 60px; white-space: nowrap;
  }
  .title .lead { font-size: 52px; }
  .title .joiner { font-family: "Parisienne", cursive; font-size: 38px; }
  .name-panel { position: absolute; left: 160px; top: 258px; width: 472px; height: 182px; }
  .certify {
    position: absolute; left: 160px; top: 292px; width: 472px; text-align: center;
    font-family: "Parisienne", cursive; font-size: 22px; line-height: 28px; color: var(--gold);
  }
  .name-line { position: absolute; left: 208px; top: 402px; width: 376px; height: 1px; background: var(--gold); }
  .statement {
    position: absolute; left: 106px; top: 524px; width: 580px; text-align: center;
    font-family: "Cormorant Garamond", serif; font-weight: 500; font-size: 15.5px; line-height: 20.5px; color: var(--white);
  }
  .field { position: absolute; top: 626px; width: 212px; height: 48px; background: rgba(255,255,255,.45); }
  .field-date { left: 160px; }
  .field-signature { left: 424px; }
  .sign-rule { position: absolute; left: 160px; top: 687px; width: 476px; height: 1px; background: var(--gold-light); }
  .date-label, .signatory {
    position: absolute; top: 692px; font-family: "Cormorant Garamond", serif; font-size: 10.5px; line-height: 13.5px; color: var(--white);
  }
  .date-label { left: 160px; }
  .signatory { left: 436px; width: 200px; text-align: right; }
  .brand {
    position: absolute; left: 670px; top: 632px; width: 240px; text-align: center;
    font-family: "Cormorant Garamond", serif; font-weight: 400; font-size: 40px; line-height: 48px; color: var(--white);
  }
</style>
</head>
<body>
<main class="canvas">
  <section class="certificate">
    <div class="imagery" role="img" aria-label="Soft pink beauty portrait photograph with flowing hair and glowing skin"></div>

    <svg class="frame" viewBox="0 0 976 756" aria-hidden="true">
      <rect x="10" y="10" width="956" height="736" fill="none" stroke="var(--gold-light)" stroke-width="2"/>
      <path d="M10 120 Q10 10 120 10" fill="none" stroke="var(--gold)" stroke-width="6"/>
      <path d="M856 10 Q966 10 966 120" fill="none" stroke="var(--gold)" stroke-width="6"/>
      <path d="M10 636 Q10 746 120 746" fill="none" stroke="var(--gold)" stroke-width="6"/>
      <path d="M856 746 Q966 746 966 636" fill="none" stroke="var(--gold)" stroke-width="6"/>
    </svg>

    <h1 class="title"><span class="lead">C</span>ERTIFICATE <span class="joiner">of</span> <span class="lead">E</span>XCELLENCE</h1>

    <svg class="name-panel" viewBox="0 0 472 182" aria-hidden="true">
      <path d="M22 6 H450 L466 24 V158 L450 176 H22 L6 158 V24 Z" fill="var(--panel)" stroke="var(--gold)" stroke-width="5"/>
      <path d="M28 13 H444 L458 28 V154 L444 169 H28 L14 154 V28 Z" fill="none" stroke="var(--gold-light)" stroke-width="1"/>
    </svg>
    <p class="certify">this is to certify that</p>
    <div class="name-line"></div>

    <p class="statement">Has successfully proven to be an<br>Artist of the Highest Standard in Eyebrow Micropigmentation<br>using the LASH VELLORA ACADEMY® Microblading Method</p>

    <div class="field field-date"></div>
    <div class="field field-signature"></div>
    <div class="sign-rule"></div>
    <p class="date-label">date</p>
    <p class="signatory">Mara Elise Vont<br>Master Instructor<br>Lash Vellora Academy®</p>

    <p class="brand">Lash Vellora</p>
  </section>
</main>
</body>
</html>
```